Business card logo

Hello, I would like a business card for my law firm with a logo composed of my initials "CV". The logo is intended to appear on my business card, my letterhead, envelope and documents from my office. My first and last name (Camille Vautrin) and "Lawyer" must appear next to the logo. I would like the logo and the characters to be in golden color on a dark background (example black, navy blue). I would especially like a refined work on the logo which should be composed of the letters J and R.

```html
<!DOCTYPE html>
<html lang="en">
<head>
<meta charset="utf-8">
<title>Camille Vautrin – Business Card</title>
<link rel="stylesheet" href="https://fonts.googleapis.com/css2?family=Cinzel:wght@500;600&family=Arimo:wght@400&display=swap">
<style>
  :root {
    --backdrop: #d6d6d8;
    --card-dark: #0f1a2e;
    --card-dark-deep: #08101f;
    --gold: #e4b645;
    --gold-light: #f3d27a;
    --gold-deep: #c8931f;
    --light-text: #e6e2d8;
  }
  * { box-sizing: border-box; margin: 0; padding: 0; }
  html, body { width: 1200px; height: 900px; overflow: hidden; }
  body {
    background: radial-gradient(ellipse at 50% 40%, #e4e4e6 0%, var(--backdrop) 100%);
    position: relative;
    font-family: "Arimo", Arial, sans-serif;
  }
  .card {
    position: absolute;
    width: 560px;
    height: 320px;
    border-radius: 24px;
    box-shadow: 0 12px 26px rgba(0,0,0,0.25);
    overflow: hidden;
    background: linear-gradient(160deg, var(--card-dark) 0%, var(--card-dark-deep) 100%);
    color: var(--gold);
  }
  .card--front {
    left: 60px; top: 110px;
    display: flex; flex-direction: column; align-items: center; justify-content: center;
  }
  .card--back { left: 580px; top: 470px; }
  .wordmark {
    display: flex; align-items: center; gap: 14px;
    font-family: "Cinzel", Georgia, serif;
    font-weight: 600;
    white-space: nowrap;
    background: linear-gradient(180deg, var(--gold-light), var(--gold-deep));
    -webkit-background-clip: text; background-clip: text;
    color: var(--gold);
  }
  .wordmark__square { width: 22px; height: 22px; background: var(--gold); flex: none; }
  .card--front .wordmark { font-size: 36px; letter-spacing: 1px; }
  .tagline {
    display: flex; align-items: center; gap: 10px;
    font-family: "Cinzel", Georgia, serif;
    font-size: 11px; letter-spacing: 8px;
    margin-top: 8px;
    color: var(--gold);
  }
  .tagline::before, .tagline::after {
    content: ""; width: 56px; height: 1px; background: currentColor;
  }
  .card--back .brand { position: absolute; left: 36px; top: 40px; }
  .card--back .wordmark { font-size: 26px; gap: 12px; }
  .card--back .wordmark__square { width: 20px; height: 20px; }
  .card--back .tagline { font-size: 9px; letter-spacing: 6px; margin-left: 32px; }
  .person { position: absolute; left: 36px; top: 150px; }
  .person__name {
    font-family: "Cinzel", Georgia, serif; font-weight: 500;
    color: var(--gold); font-size: 20px; letter-spacing: 1px;
  }
  .person__role { font-size: 14px; color: var(--light-text); margin-top: 2px; }
  .contact { list-style: none; margin-top: 12px; }
  .contact li {
    display: flex; align-items: center; gap: 10px;
    font-size: 14px; color: var(--light-text); line-height: 20px;
  }
  .contact svg { width: 13px; height: 13px; fill: var(--gold); flex: none; }
  .address {
    position: absolute; right: 34px; top: 150px;
    text-align: right; font-size: 13px; color: var(--light-text);
    line-height: 18px; font-style: normal;
  }
</style>
</head>
<body>
  <section class="card card--front">
    <div class="wordmark"><span class="wordmark__square"></span>Camille Vautrin</div>
    <div class="tagline">Lawyer</div>
  </section>

  <section class="card card--back">
    <div class="brand">
      <div class="wordmark"><span class="wordmark__square"></span>Camille Vautrin</div>
      <div class="tagline">Lawyer</div>
    </div>

    <div class="person">
      <p class="person__name">Mathis Laurent</p>
      <p class="person__role">Managing Director</p>
      <ul class="contact">
        <li><svg viewBox="0 0 16 16"><path d="M2 3c0-1 1-2 2-2h2l1 4-2 1c1 2 3 4 5 5l1-2 4 1v2c0 1-1 2-2 2C7 14 2 9 2 3z"/></svg>031-845 270 614</li>
        <li><svg viewBox="0 0 16 16"><path d="M4 1h8v14H4zM5.5 2.5v9h5v-9z" fill-rule="evenodd"/></svg>031-845 270 615</li>
        <li><svg viewBox="0 0 16 16"><path d="M1 3h14v10H1zM2 4l6 5 6-5z" fill-rule="evenodd"/></svg>contact@vautrin-avocat.fr</li>
        <li><svg viewBox="0 0 16 16"><circle cx="8" cy="8" r="7"/></svg>www.vautrin-avocat.fr</li>
      </ul>
    </div>

    <address class="address">
      18, Rue des Tanneurs<br>Lyon, France 69002
    </address>
  </section>
</body>
</html>
```